Occupational Therapy promotional poster

We need 2 x A4 posters to be created:
- 1 with a male super hero
- 1 with a female super hero (see suggested design).

These posters will be used for a promotional campaign celebrating occupational therapy. The idea being that occupational therapists are our local superhero. We see them as the ‘unsung heroes’ of our local communities, so this campaign is a play on that idea.

These posters will be displayed on community notice boards and in hospitals. They will also be used on display tables promoting what occupational therapy is. They will also potentially be used as handouts in presentations. We plan to use these posters for the coming 2 years.

As these will be displayed on noticeboards they need to be bright and colourful. The colours suggested in the attachment are the types of colours we would like used (blue, yellow and red).

We envision these posters being displayed side by side.

Although we are open to interpretation of the “super hero” theme – we particularly liked the black super hero images as they look similar to the symbol for wheelchair access (which occupational therapists use).

Alternatively, a comic book inspired design would also be appealing – see inspiration images in attached document.

See the images that we have drawn inspiration from. I've included the black generic super heroes as well as the comic book style.

This design needs to include the KLRV-PTB logo which is included.

The superhero also needs to have a starwarden style logo somewhere visable. This could be on their chest or on their cape – depending on their angle. Instead of the Starwarden ‘S’, please put ‘OT’.

The content for both posters is identical. However, we would like 1 male version of the poster and 1 female version of the poster.

The superhero graphic needs to be G-rated. For the female graphic - it cannot include cleavage or clothing that is too tight/revealing.

Based on the locations where the poster will be displayed, it does need to have a professional feel.

ATTACHED:
- the KLRV-PTB Logo (to be included)
- a design brief + all text that needs to be included
- an example of the type of posters that we are envisioning

Target Market(s)

General public in New Zealand: Patients in hospital waiting rooms, mothers of children in childcare, elderly people who look at notice boards

Industry/Entity Type

Health Care

Font styles to use
Sans Serif

Requirements
Must have
• 2 A4 twin posters. Identical content but 1 female version and 1 male version
• The KLRV-PTB logo (attached)
• A "superhero" symbol on the chest or cape of the superhero. It should look like the starwarden symbol but instead say "OT" rather than S.
• Must be bright and colourful
• Must include all text included
Should not have
• Any nudity, revealing poses or tight clothing. G-rated.

```html
<!DOCTYPE html>
<html lang="en">
<head>
<meta charset="utf-8">
<title>Meet Your Local Superhero – The Occupational Therapist</title>
<link rel="stylesheet" href="https://fonts.googleapis.com/css2?family=Roboto:ital,wght@0,400;0,500;0,700;0,900;1,400&family=Roboto+Condensed:wght@700;900&display=swap">
<style>
  :root {
    --red: #e1251b;
    --red-deep: #c81a12;
    --orange: #f15a22;
    --yellow: #ffd200;
    --white: #ffffff;
    --ink: #222222;
    --hero-dark: #1c1c1c;
  }
  * { box-sizing: border-box; margin: 0; padding: 0; }
  html, body { width: 851px; height: 1200px; overflow: hidden; background: var(--white); }
  body { font-family: "Roboto", Arial, sans-serif; color: var(--ink); }

  .poster {
    width: 851px; height: 1200px; overflow: hidden; background: var(--white);
    display: flex; flex-direction: column;
  }

  .masthead {
    background: var(--red); height: 62px;
    display: flex; align-items: center; justify-content: center;
  }
  .masthead h1 {
    font-family: "Roboto Condensed", "Arial Narrow", sans-serif;
    font-weight: 900; color: var(--white); font-size: 46px; letter-spacing: 0.5px;
  }
  .subhead {
    background: var(--yellow); height: 54px;
    display: flex; align-items: center; justify-content: center;
  }
  .subhead h2 {
    font-family: "Roboto Condensed", "Arial Narrow", sans-serif;
    font-weight: 700; color: var(--red); font-size: 34px;
  }

  .intro { padding: 14px 34px 0; font-style: italic; font-size: 15px; line-height: 1.4; }
  .section-bar {
    margin-top: 10px; background: var(--red); color: var(--white);
    font-weight: 700; font-size: 14px; text-transform: uppercase; padding: 4px 34px;
  }
  .section-text { padding: 8px 34px 0; font-size: 15px; line-height: 1.4; }

  .hero-zone {
    position: relative; flex: 1; margin-top: 14px; min-height: 720px;
    background: radial-gradient(circle at 25% 35%, var(--yellow) 0%, var(--orange) 45%, var(--red) 82%);
  }
  .brand-dot {
    position: absolute; left: 22px; top: 180px;
    width: 48px; height: 48px; border-radius: 50%; background: var(--white);
  }
  .hero-figure {
    position: absolute; left: 80px; top: 30px; width: 220px; height: 470px;
    background: linear-gradient(160deg, var(--hero-dark) 0%, var(--hero-dark) 55%, var(--red-deep) 100%);
    border-radius: 110px 110px 20px 20px; opacity: 0.92;
  }

  .profile {
    position: absolute; left: 306px; top: 28px; width: 516px;
    background: var(--white); border: 4px solid var(--red); padding-bottom: 14px;
  }
  .profile h3 {
    background: var(--red); color: var(--yellow);
    font-family: "Roboto Condensed", "Arial Narrow", sans-serif;
    font-weight: 900; font-size: 28px; padding: 6px 18px;
  }
  .profile p { padding: 10px 18px 4px; font-size: 16px; font-weight: 700; }
  .profile ul { list-style: none; padding: 0 18px; }
  .profile li {
    position: relative; padding-left: 18px; font-size: 16px; line-height: 1.3; margin-bottom: 4px;
  }
  .profile li::before {
    content: ""; position: absolute; left: 2px; top: 7px;
    width: 7px; height: 7px; border-radius: 50%; background: var(--red);
  }

  .call-to-action {
    position: absolute; left: 34px; top: 560px; width: 580px;
    color: var(--white); font-size: 23px; line-height: 1.35; font-weight: 700;
  }
  .call-to-action strong { color: var(--yellow); font-family: "Roboto Condensed", sans-serif; font-weight: 900; font-size: 30px; }
  .call-to-action .tag { color: var(--yellow); }

  .client-mark {
    position: absolute; left: 636px; top: 520px; width: 190px; height: 150px;
    background: var(--white); border: 3px solid var(--red);
    display: flex; flex-direction: column; align-items: center; justify-content: center; gap: 10px;
  }
  .client-mark .square { width: 36px; height: 36px; background: var(--red); }
  .client-mark span { font-weight: 700; font-size: 22px; color: var(--red); }
</style>
</head>
<body>
<main class="poster">
  <header>
    <div class="masthead"><h1>MEET YOUR LOCAL SUPERHERO</h1></div>
    <div class="subhead"><h2>THE OCCUPATIONAL THERAPIST</h2></div>
  </header>

  <p class="intro">Imagine being defeated by an everyday task like putting your clothes on, catching a bus, spending time with your friends or taking care of yourself.</p>

  <div class="section-bar">Occupational therapy is here to help.</div>
  <p class="section-text">The things that you do – your occupations – help express who you are, how you feel about yourself, and how you connect with others. Your health and wellbeing will be affected if you are unable to do the things you want and need to do, to live and enjoy your life.</p>

  <div class="section-bar">Occupational therapists help people of all ages and work in a variety of settings.</div>
  <p class="section-text">Occupations that could cause difficulty include preparing and eating meals; driving and mobility; recreation and exercise; use of a computer or workstation; showering or bathing; getting things done on time and in a preferred standard; having enough things to do and the confidence to do them; developing supportive relationships or friendships; or thriving in school.</p>

  <section class="hero-zone">
    <div class="brand-dot"></div>
    <div class="hero-figure" role="img" aria-label="Black silhouette of a caped superhero with a red cape and an OT shield on the chest"></div>

    <div class="profile">
      <h3>SUPERHERO PROFILE</h3>
      <p>My super powers help people to:</p>
      <ul>
        <li>Learn new ways of doing things following an illness or injury (e.g. dressing or cooking)</li>
        <li>Thrive in their senior years</li>
        <li>Regulate their strong emotions</li>
        <li>Achieve their goals at school</li>
        <li>Develop ways to manage pain</li>
        <li>Develop their confidence in social situations</li>
        <li>Access support available in the community</li>
        <li>Adapt material or equipment (e.g. wheel chairs or provide a special bath or toilet seat)</li>
        <li>Make changes to their living or working environment</li>
        <li>Develop new skills, abilities or interests (e.g. job readiness programmes)</li>
      </ul>
    </div>

    <p class="call-to-action"><strong>JOIN US</strong> in celebrating occupational therapy by using the hashtag <span class="tag">#YourLocalSuperHero</span><br>Visit <span class="tag">klrvptb.co.nz</span> for more information</p>

    <div class="client-mark"><div class="square"></div><span>KLRV-PTB</span></div>
  </section>
</main>
</body>
</html>
```